Manufacturer Needs Custom Village Weave Ecommerce Site

We work with local artisans in remote villages around the world to create unique and culturally authentic weaved baskets - decorative, storage, laundry, and handbags.

```html
<!DOCTYPE html>
<html lang="en">
<head>
<meta charset="utf-8">
<title>Village Weave – Homepage Concepts</title>
<link href="https://fonts.googleapis.com/css2?family=Lobster&family=Poppins:wght@400;600&display=swap" rel="stylesheet">
<style>
  :root{
    --stage:#4a4a4a;
    --red:#e5202e;
    --black:#111111;
    --dark:#1c1c1c;
    --white:#ffffff;
    --light:#eeeeee;
    --text:#555555;
    --muted:#9a9a9a;
    --script:"Lobster", cursive;
    --sans:"Poppins", sans-serif;
  }
  *{box-sizing:border-box;margin:0;padding:0}
  html,body{width:811px;height:1200px;overflow:hidden}
  body{background:var(--stage);font-family:var(--sans);position:relative}

  .page{position:absolute;top:49px;width:368px;background:var(--white);overflow:hidden}
  .page--a{left:19px}
  .page--b{left:416px}

  /* header */
  .site-header{height:19px;background:var(--black);display:flex;align-items:center;justify-content:space-between;padding:0 14px}
  .brand{font-family:var(--sans);font-weight:600;font-size:8px;color:var(--red);display:flex;align-items:center;gap:4px}
  .brand-dot{width:5px;height:5px;border-radius:50%;background:var(--red)}
  .main-nav{display:flex;gap:9px;align-items:center;font-size:4.5px;color:var(--white)}
  .main-nav svg{width:7px;height:7px}

  /* hero */
  .hero{height:183px;position:relative;display:flex;flex-direction:column;align-items:center;justify-content:center;gap:10px}
  .hero-photo{position:absolute;inset:0}
  .page--a .hero-photo{background:linear-gradient(120deg,#e85a8a 0%,#f2b640 30%,#3fb1c9 55%,#e2683a 80%,#7ac36a 100%)}
  .page--b .hero-photo{background:linear-gradient(135deg,#2f4a2c 0%,#6b5a35 40%,#b98a52 65%,#3b3f28 100%)}
  .hero-title{position:relative;font-family:var(--script);font-size:17px;color:var(--white);text-align:center;line-height:1.1;max-width:170px;text-shadow:0 1px 3px rgba(0,0,0,.4)}
  .btn{display:inline-block;background:var(--red);color:var(--white);font-size:4.5px;font-weight:600;padding:3px 10px;border-radius:8px;position:relative}

  /* headings */
  .section-title{font-family:var(--script);font-size:15px;color:var(--black);text-align:center}
  .section-title .accent{color:var(--red)}
  .on-dark .section-title{color:var(--white)}
  .copy{font-size:4.5px;line-height:1.7;color:var(--text)}

  /* about */
  .about{height:181px;display:flex;align-items:center;gap:16px;padding:0 20px}
  .framed{position:relative;flex:none}
  .framed::after{content:"";position:absolute;left:6px;top:6px;right:-6px;bottom:-6px;border:1.5px solid var(--red);z-index:0}
  .framed .photo{position:relative;z-index:1;width:100%;height:100%}
  .about .framed{width:168px;height:118px}
  .baskets-photo{background:linear-gradient(90deg,#e9b9d0,#f4d36b,#8fcfe0,#f19a5f,#c5e28c)}
  .about-body{display:flex;flex-direction:column;gap:8px}
  .about-body .section-title{text-align:left}

  /* arrivals */
  .arrivals{height:176px;background:var(--dark);padding-top:14px}
  .card-row{display:flex;gap:12px;justify-content:center;margin-top:12px}
  .arrival-card{width:78px;background:var(--white);padding:5px}
  .arrival-card h3{font-size:5px;font-weight:600;color:var(--black);text-align:center;margin-bottom:4px}
  .arrival-card .photo{height:92px}
  .p1{background:linear-gradient(160deg,#d89b5b,#a06a3a)}
  .p2{background:linear-gradient(160deg,#7fb8c9,#e6c48a)}
  .p3{background:linear-gradient(160deg,#e0728f,#f2c14e)}

  /* how */
  .how{height:202px;padding:16px 20px 0}
  .how-row{display:flex;gap:18px;align-items:center;margin-top:14px}
  .how-body{flex:1;display:flex;flex-direction:column;gap:10px;align-items:flex-start}
  .how .framed{width:140px;height:130px}
  .page--a .weaver-photo{background:linear-gradient(140deg,#3c5b6b,#c58f55,#e7c78e)}
  .page--b .weaver-photo{background:linear-gradient(140deg,#f7f1e6,#f2a7c0,#8fd2d8)}

  /* gallery */
  .gallery{height:162px;padding-top:12px}
  .page--a .gallery{background:var(--light)}
  .page--b .gallery{background:var(--black)}
  .page--b .gallery .section-title{color:var(--white)}
  .gallery-photo{height:112px;margin:10px 20px 0;background:linear-gradient(100deg,#6b4a2b,#c89a5c 35%,#e7b24c 55%,#8a5a34 80%,#4d3320)}

  /* products */
  .products{height:108px;padding-top:10px;position:relative}
  .product-row{display:flex;gap:8px;justify-content:center;margin-top:8px}
  .product-card{width:60px;border:0.8px solid #dddddd;padding:3px;text-align:center}
  .product-card .photo{height:30px;margin-bottom:3px}
  .product-card h4{font-size:4px;font-weight:600;color:var(--black)}
  .product-card .price{font-size:4px;color:var(--red);margin:1px 0 3px}
  .product-card .btn{font-size:3.5px;padding:2px 6px}
  .q1{background:linear-gradient(135deg,#f3c35b,#d9773c)}
  .q2{background:linear-gradient(135deg,#8fcbd6,#e3e0c2)}
  .q3{background:linear-gradient(135deg,#d9a06b,#9b6b3d)}
  .q4{background:linear-gradient(135deg,#e98fa9,#f6d57f)}
  .arrow{position:absolute;top:62px;width:6px;height:10px}
  .arrow--prev{left:8px}
  .arrow--next{right:8px}

  /* footer */
  .site-footer{height:68px;background:var(--black);padding:10px 26px 0;position:relative}
  .footer-cols{display:flex;justify-content:space-between}
  .footer-col h5{font-size:4.5px;color:var(--white);font-weight:600;margin-bottom:4px;padding-left:4px;border-left:1.5px solid var(--red)}
  .footer-col li{list-style:none;font-size:3.8px;color:var(--muted);line-height:1.8;padding-left:5px}
  .legal{position:absolute;left:0;right:0;bottom:0;height:12px;border-top:1px solid var(--red);font-size:3.8px;color:var(--muted);display:flex;align-items:center;justify-content:center;gap:4px}
</style>
</head>
<body>

<!-- concept A -->
<article class="page page--a">
  <header class="site-header">
    <div class="brand"><span class="brand-dot"></span>Village Weave</div>
    <nav class="main-nav"><span>Home</span><span>About</span><span>Shop</span><span>Gallery</span><span>Contact</span>
      <svg viewBox="0 0 10 10"><path d="M1 2h1.5l1.2 5h4.5l1-3.5H3" fill="none" stroke="#fff" stroke-width="0.9"/><circle cx="4.3" cy="8.6" r=".7" fill="#fff"/><circle cx="7.6" cy="8.6" r=".7" fill="#fff"/></svg>
    </nav>
  </header>
  <section class="hero">
    <div class="hero-photo" role="img" aria-label="Colourful woven baskets stacked at a village market"></div>
    <h1 class="hero-title">We Make Things With Love</h1>
    <a class="btn">Shop Now</a>
  </section>
  <section class="about">
    <div class="framed"><div class="photo baskets-photo" role="img" aria-label="Rows of brightly striped woven baskets"></div></div>
    <div class="about-body">
      <h2 class="section-title">About <span class="accent">Us</span></h2>
      <p class="copy">We partner with village artisans around the world to weave each basket by hand, keeping old craft traditions alive.</p>
      <div><a class="btn">Read More</a></div>
    </div>
  </section>
  <section class="arrivals on-dark">
    <h2 class="section-title"><span class="accent">Our</span> New Arrivals</h2>
    <div class="card-row">
      <div class="arrival-card"><h3>Decorative</h3><div class="photo p1" role="img" aria-label="Decorative woven basket"></div></div>
      <div class="arrival-card"><h3>Storage</h3><div class="photo p2" role="img" aria-label="Storage basket with lid"></div></div>
      <div class="arrival-card"><h3>Handbags</h3><div class="photo p3" role="img" aria-label="Woven handbag"></div></div>
    </div>
  </section>
  <section class="how">
    <h2 class="section-title">How <span class="accent">We Do?</span></h2>
    <div class="how-row">
      <div class="how-body">
        <p class="copy">Every basket starts with local grass, palm or reed, dyed in bright colours and woven slowly by skilled hands.</p>
        <a class="btn">Learn More</a>
      </div>
      <div class="framed"><div class="photo weaver-photo" role="img" aria-label="Artisan weaving a basket by hand"></div></div>
    </div>
  </section>
  <section class="gallery">
    <h2 class="section-title">Our <span class="accent">Gallery</span></h2>
    <div class="gallery-photo" role="img" aria-label="Market stall filled with woven baskets"></div>
  </section>
  <section class="products">
    <h2 class="section-title">Latest <span class="accent">Products</span></h2>
    <svg class="arrow arrow--prev" viewBox="0 0 6 10"><path d="M5 1L1 5l4 4" fill="none" stroke="#333" stroke-width="1.2"/></svg>
    <div class="product-row">
      <div class="product-card"><div class="photo q1" role="img" aria-label="Market tote basket"></div><h4>Market Tote</h4><p class="price">$24</p><a class="btn">Buy Now</a></div>
      <div class="product-card"><div class="photo q2" role="img" aria-label="Laundry hamper"></div><h4>Laundry Hamper</h4><p class="price">$38</p><a class="btn">Buy Now</a></div>
      <div class="product-card"><div class="photo q3" role="img" aria-label="Storage bin"></div><h4>Storage Bin</h4><p class="price">$29</p><a class="btn">Buy Now</a></div>
      <div class="product-card"><div class="photo q4" role="img" aria-label="Fruit bowl basket"></div><h4>Fruit Bowl</h4><p class="price">$19</p><a class="btn">Buy Now</a></div>
    </div>
    <svg class="arrow arrow--next" viewBox="0 0 6 10"><path d="M1 1l4 4-4 4" fill="none" stroke="#333" stroke-width="1.2"/></svg>
  </section>
  <footer class="site-footer">
    <div class="footer-cols">
      <div class="footer-col"><h5>Shop</h5><ul><li>Baskets</li><li>Handbags</li><li>Storage</li></ul></div>
      <div class="footer-col"><h5>Company</h5><ul><li>About</li><li>Artisans</li><li>Blog</li></ul></div>
      <div class="footer-col"><h5>Help</h5><ul><li>Shipping</li><li>Returns</li><li>FAQ</li></ul></div>
      <div class="footer-col"><h5>Follow</h5><ul><li>Newsletter</li><li>Journal</li><li>Events</li></ul></div>
    </div>
    <div class="legal">© 2024 Village Weave · All rights reserved</div>
  </footer>
</article>

<!-- concept B -->
<article class="page page--b">
  <header class="site-header">
    <div class="brand"><span class="brand-dot"></span>Village Weave</div>
    <nav class="main-nav"><span>Home</span><span>About</span><span>Shop</span><span>Gallery</span><span>Contact</span>
      <svg viewBox="0 0 10 10"><path d="M1 2h1.5l1.2 5h4.5l1-3.5H3" fill="none" stroke="#fff" stroke-width="0.9"/><circle cx="4.3" cy="8.6" r=".7" fill="#fff"/><circle cx="7.6" cy="8.6" r=".7" fill="#fff"/></svg>
    </nav>
  </header>
  <section class="hero">
    <div class="hero-photo" role="img" aria-label="Artisan seated among handmade baskets outdoors"></div>
    <h1 class="hero-title">We Make Things With Love</h1>
    <a class="btn">Shop Now</a>
  </section>
  <section class="about">
    <div class="framed"><div class="photo baskets-photo" role="img" aria-label="Rows of brightly striped woven baskets"></div></div>
    <div class="about-body">
      <h2 class="section-title">About <span class="accent">Us</span></h2>
      <p class="copy">We partner with village artisans around the world to weave each basket by hand, keeping old craft traditions alive.</p>
      <div><a class="btn">Read More</a></div>
    </div>
  </section>
  <section class="arrivals on-dark">
    <h2 class="section-title"><span class="accent">Our</span> New Arrivals</h2>
    <div class="card-row">
      <div class="arrival-card"><h3>Decorative</h3><div class="photo p1" role="img" aria-label="Decorative woven basket"></div></div>
      <div class="arrival-card"><h3>Storage</h3><div class="photo p2" role="img" aria-label="Storage basket with lid"></div></div>
      <div class="arrival-card"><h3>Handbags</h3><div class="photo p3" role="img" aria-label="Woven handbag"></div></div>
    </div>
  </section>
  <section class="how">
    <h2 class="section-title">How <span class="accent">We Do?</span></h2>
    <div class="how-row">
      <div class="how-body">
        <p class="copy">Every basket starts with local grass, palm or reed, dyed in bright colours and woven slowly by skilled hands.</p>
        <a class="btn">Learn More</a>
      </div>
      <div class="framed"><div class="photo weaver-photo" role="img" aria-label="Pastel baskets arranged on a light table"></div></div>
    </div>
  </section>
  <section class="gallery on-dark">
    <h2 class="section-title">Our <span class="accent">Gallery</span></h2>
    <div class="gallery-photo" role="img" aria-label="Market stall filled with woven baskets"></div>
  </section>
  <section class="products">
    <h2 class="section-title">Latest <span class="accent">Products</span></h2>
    <svg class="arrow arrow--prev" viewBox="0 0 6 10"><path d="M5 1L1 5l4 4" fill="none" stroke="#333" stroke-width="1.2"/></svg>
    <div class="product-row">
      <div class="product-card"><div class="photo q1" role="img" aria-label="Market tote basket"></div><h4>Market Tote</h4><p class="price">$24</p><a class="btn">Buy Now</a></div>
      <div class="product-card"><div class="photo q2" role="img" aria-label="Laundry hamper"></div><h4>Laundry Hamper</h4><p class="price">$38</p><a class="btn">Buy Now</a></div>
      <div class="product-card"><div class="photo q3" role="img" aria-label="Storage bin"></div><h4>Storage Bin</h4><p class="price">$29</p><a class="btn">Buy Now</a></div>
      <div class="product-card"><div class="photo q4" role="img" aria-label="Fruit bowl basket"></div><h4>Fruit Bowl</h4><p class="price">$19</p><a class="btn">Buy Now</a></div>
    </div>
    <svg class="arrow arrow--next" viewBox="0 0 6 10"><path d="M1 1l4 4-4 4" fill="none" stroke="#333" stroke-width="1.2"/></svg>
  </section>
  <footer class="site-footer">
    <div class="footer-cols">
      <div class="footer-col"><h5>Shop</h5><ul><li>Baskets</li><li>Handbags</li><li>Storage</li></ul></div>
      <div class="footer-col"><h5>Company</h5><ul><li>About</li><li>Artisans</li><li>Blog</li></ul></div>
      <div class="footer-col"><h5>Help</h5><ul><li>Shipping</li><li>Returns</li><li>FAQ</li></ul></div>
      <div class="footer-col"><h5>Follow</h5><ul><li>Newsletter</li><li>Journal</li><li>Events</li></ul></div>
    </div>
    <div class="legal">© 2024 Village Weave · All rights reserved</div>
  </footer>
</article>

</body>
</html>
```